Buff & Gleam

polished concrete and epoxy coatings flooring company

Target Market(s)

Industrial commercial

Industry/Entity Type

Industrial flooring contractor

Contact Information for Business Card

POLISHED CONCRETE • EPOXY COATING • TERRAZZO RESTORATION • SHOT BLASTING • SURFACE PREPARATION • JOINT FILLING • TILE/ CARPET /GLUE REMOVAL

Colors
0054AA
0677BA
7BADD7
CADEEF
E8F1F8

Requirements
Must have
• email buffandgleamfloors@mailbrook.example Address 47215 Tallowmere Rd, Fraser, MI 48093. Name Ray Tulvin. Services Polished concrete- Epoxy Coatings- Terrazzo restoration-surface preparation- safety striping- joint filling- tile/ carpet/ glue removal phone number 586-700-3926 email buffandgleamfloors.example
Nice to have
• Instagram Facebook logo maybe smaller in the corner

```html
<!DOCTYPE html>
<html lang="en">
<head>
<meta charset="UTF-8">
<title>Buff &amp; Gleam – Business Card</title>
<link href="https://fonts.googleapis.com/css2?family=Cinzel:wght@400&family=Oswald:wght@500&family=Roboto:wght@400;500&display=swap" rel="stylesheet">
<style>
  :root {
    --stage: #2b2c2e;
    --card: #1e1f21;
    --card-band: #1a1b1d;
    --blue: #0677ba;
    --blue-deep: #0054aa;
    --white: #ffffff;
    --rule: #e8f1f8;
  }
  * { box-sizing: border-box; margin: 0; padding: 0; }
  html, body { width: 1200px; height: 840px; overflow: hidden; }
  body {
    background: var(--stage);
    display: flex; flex-direction: column; align-items: center; justify-content: center;
    gap: 56px;
    font-family: "Roboto", Arial, sans-serif;
    color: var(--white);
  }
  .card {
    position: relative;
    width: 600px; height: 343px;
    background: var(--card);
    border-radius: 22px;
    border-bottom: 5px solid var(--blue);
    border-left: 2px solid var(--blue);
    overflow: hidden;
  }

  /* Back side */
  .lower-band {
    position: absolute; left: 0; right: 0; bottom: 0; height: 46%;
    background: var(--card-band);
  }
  .services {
    position: absolute; left: 0; right: 0; top: 50%;
    transform: translateY(-50%);
    text-align: center;
  }
  .services-heading {
    display: flex; align-items: center; justify-content: center; gap: 10px;
    font-family: "Oswald", Arial, sans-serif; font-weight: 500;
    color: var(--blue); font-size: 22px; letter-spacing: 0.5px;
    margin-bottom: 10px;
  }
  .services-heading::before, .services-heading::after {
    content: ""; width: 190px; height: 1px; background: var(--rule);
  }
  .services-line { font-size: 17px; line-height: 1.5; }
  .dot { color: var(--blue); padding: 0 2px; }

  /* Front side */
  .brand {
    position: absolute; left: 0; right: 0; top: 46px; text-align: center;
  }
  .brand-name {
    font-family: "Roboto", Arial, sans-serif; font-weight: 500;
    font-size: 44px; color: var(--white); letter-spacing: 2px; line-height: 1.1;
  }
  .brand-tagline {
    font-family: "Oswald", Arial, sans-serif; font-weight: 500;
    color: var(--blue); font-size: 16px; letter-spacing: 1px; margin-top: 6px;
  }
  .contact-row {
    position: absolute; left: 28px; right: 28px; top: 166px;
    display: flex; align-items: center; justify-content: center;
  }
  .person-name {
    font-family: "Cinzel", Georgia, serif; font-weight: 400;
    color: var(--blue); font-size: 32px; white-space: nowrap;
    padding-right: 16px;
  }
  .divider { width: 1px; height: 76px; background: var(--rule); margin-right: 14px; flex: none; }
  .contact-list { list-style: none; font-size: 14px; line-height: 1.7; }
  .contact-list li { display: flex; align-items: center; gap: 7px; white-space: nowrap; }
  .contact-list svg { width: 14px; height: 14px; fill: var(--blue); flex: none; }
  .address {
    position: absolute; left: 0; right: 0; bottom: 38px;
    text-align: center; font-size: 17px;
  }
</style>
</head>
<body>

  <section class="card card-back" aria-label="Card back: services">
    <div class="lower-band" aria-hidden="true"></div>
    <div class="services">
      <h2 class="services-heading">SERVICES</h2>
      <p class="services-line"><span class="dot">•</span>Polished concrete <span class="dot">•</span> Epoxy Coatings</p>
      <p class="services-line"><span class="dot">•</span>Terrazzo restoration <span class="dot">•</span> surface preparation <span class="dot">•</span> safety striping</p>
      <p class="services-line"><span class="dot">•</span>joint filling <span class="dot">•</span> tile/ carpet/ glue removal</p>
    </div>
  </section>

  <section class="card card-front" aria-label="Card front: contact">
    <div class="brand">
      <h1 class="brand-name">BUFF &amp; GLEAM</h1>
      <p class="brand-tagline">INNOVATIVE CONCRETE FLOORING</p>
    </div>
    <div class="contact-row">
      <p class="person-name">RAY TULVIN</p>
      <span class="divider"></span>
      <ul class="contact-list">
        <li><svg viewBox="0 0 16 16" aria-hidden="true"><path d="M3.6 1.2l2.3 2.6-1.2 1.8c.9 2 2.5 3.6 4.5 4.5l1.8-1.2 2.6 2.3-1.1 2.4C7.2 13.4 2.6 8.8 1.2 3.5z"/></svg>586-700-3926</li>
        <li><svg viewBox="0 0 16 16" aria-hidden="true"><path d="M1 3h14v10H1zM2.2 4.2v.4L8 8.8l5.8-4.2v-.4zM2.2 6v5.8h11.6V6L8 10.2z"/></svg>buffandgleamfloors@mailbrook.example</li>
        <li><svg viewBox="0 0 16 16" aria-hidden="true"><path d="M8 1a7 7 0 100 14A7 7 0 008 1zm-.8 1.8v2.4H5.6A5.4 5.4 0 017.2 2.8zm1.6 0a5.4 5.4 0 011.6 2.4H8.8zM4.2 6.8h3v2.4h-3a5 5 0 010-2.4zm4.6 0h3a5 5 0 010 2.4h-3zm-3.2 4h1.6v2.4a5.4 5.4 0 01-1.6-2.4zm3.2 0h1.6a5.4 5.4 0 01-1.6 2.4z"/></svg>buffandgleamfloors.example</li>
      </ul>
    </div>
    <p class="address">47215 Tallowmere Rd, Fraser, MI 48093</p>
  </section>

</body>
</html>
```